International PR and marketing agency needs website design

We need a branding website, for a company based in the US (Washington DC). We are a communication (PR, marketing, social media) agency. We already have the copy, and we have some example websites (some major agencies), that we like.
For example:
https://tallorquinbeam.example/
https://zurvexglobal.example/
https://pemrat.example/
https://qfn-omnis.example/
https://www.roskavert.example/
The website must be a multi-language site, we will add the new languages step-by-step.
We would like to upload content continuously.
The website has to have sub-pages (segments), and news part.
Target Market(s)
Global
Industry/Entity Type
Public relations, Communications, Marketing, Social Media
Number of Pages Required
5+ page
Font styles to use
Other font styles liked:
- Well readable, modern style.
Look and feel
Each slider illustrates characteristics of the customer's brand and the style your logo design should communicate.

```html
<!DOCTYPE html>
<html lang="en">
<head>
<meta charset="utf-8">
<title>Kavora PR — We Are Building Relationships</title>
<link rel="stylesheet" href="https://fonts.googleapis.com/css2?family=Lexend+Exa:wght@500;600&family=Lato:wght@400;700&family=Poppins:wght@400;500;600&display=swap">
<style>
:root{
  --ink:#1b1b1d;
  --red:#e5000f;
  --magenta:#981863;
  --white:#ffffff;
  --line:#d8d8d8;
  --footer-line:#3a3a3d;
  --chip:#333336;
  --grad:linear-gradient(90deg,var(--red),var(--magenta));
}
*{box-sizing:border-box;margin:0;padding:0}
html,body{width:1200px;height:3773px;overflow:hidden}
body{position:relative;background:var(--white);font-family:"Lato",sans-serif;color:var(--ink)}
.abs{position:absolute}
.display{font-family:"Lexend Exa",sans-serif;font-weight:600;letter-spacing:-0.04em}
.btn{position:absolute;display:flex;align-items:center;justify-content:center;gap:8px;border-radius:30px;background:var(--grad);color:var(--white);font-family:"Poppins",sans-serif;font-weight:600;font-size:14px;text-decoration:none;white-space:nowrap}
.photo{position:absolute}

/* hero */
.hero{position:absolute;left:0;top:0;width:1200px;height:765px;background:var(--ink);overflow:hidden}
.brand{position:absolute;left:88px;top:16px;display:flex;align-items:center;gap:10px}
.brand-dot{width:56px;height:56px;border-radius:50%;background:var(--grad)}
.brand-name{font-family:"Lexend Exa",sans-serif;font-weight:600;font-size:20px;color:var(--white);letter-spacing:-0.04em}
.nav{position:absolute;top:44px;left:356px;display:flex;align-items:center;gap:18px;font-family:"Poppins",sans-serif;font-weight:600;font-size:13px;line-height:16px;color:var(--white)}
.nav a{color:var(--white);text-decoration:none;white-space:nowrap;display:flex;align-items:center}
.nav .caret{color:var(--red);font-size:10px;margin-left:3px}
.flag{display:inline-block;width:20px;height:11px;background:linear-gradient(180deg,#b22 50%,#ddd 50%);margin-right:5px}
.hero-title{position:absolute;left:0;width:1200px;text-align:center;color:var(--white);font-size:88px;line-height:84px}
.hero-title .accent{background:var(--grad);-webkit-background-clip:text;background-clip:text;color:transparent}
.hero-copy{position:absolute;left:230px;width:740px;top:372px;text-align:center;color:var(--white);font-size:13px;line-height:21px}
.hero-photo{left:89px;top:527px;width:1021px;height:476px;border-radius:40px;background:linear-gradient(120deg,#cfc9c2 0%,#8a8580 35%,#e4e2de 60%,#6c6a6e 100%);box-shadow:0 20px 40px rgba(0,0,0,.15)}

/* who we are */
.who-mark{position:absolute;left:227px;top:1102px;width:311px;height:311px;border-radius:50%;background:linear-gradient(180deg,var(--red),var(--magenta));display:flex;align-items:center;justify-content:center}
.who-mark span{font-family:"Lexend Exa",sans-serif;font-weight:600;font-size:40px;color:var(--white);letter-spacing:-0.04em}
.eyebrow{font-family:"Lexend Exa",sans-serif;font-weight:500;color:var(--red);font-size:17px;letter-spacing:-0.02em}
.section-title{font-size:44px;line-height:44px}
.body-copy{font-size:13px;line-height:20.5px;color:#333}

/* expertise */
.expertise{position:absolute;left:0;top:1505px;width:1200px;height:672px;background:var(--ink);overflow:hidden}
.tile{position:absolute;top:243px;height:429px}
.tile-label{position:absolute;left:22px;bottom:62px;font-family:"Lexend Exa",sans-serif;font-weight:600;font-size:19px;line-height:22px;color:var(--white);letter-spacing:-0.04em}

/* news */
.news-card{position:absolute;top:2361px;width:331px;height:264px;border-radius:20px}
.news-caption{position:absolute;top:2652px;width:331px;text-align:center;font-family:"Lexend Exa",sans-serif;font-weight:600;font-size:22px;letter-spacing:-0.04em}

/* social */
.social-band{position:absolute;left:0;top:2836px;width:1200px;height:120px;overflow:hidden}
.social-word{position:absolute;left:-20px;top:-8px;width:1240px;text-align:center;font-family:"Lexend Exa",sans-serif;font-weight:600;font-size:170px;line-height:170px;letter-spacing:-0.06em;background:linear-gradient(180deg,#d2d2d2 0%,#efefef 55%,#ffffff 80%);-webkit-background-clip:text;background-clip:text;color:transparent;white-space:nowrap}
.social-btn{position:absolute;top:3032px;width:68px;height:68px;border-radius:50%}

/* footer */
.footer{position:absolute;left:0;top:3181px;width:1200px;height:592px;background:var(--ink);overflow:hidden;color:var(--white)}
.foot-head{position:absolute;top:262px;font-family:"Lexend Exa",sans-serif;font-weight:600;font-size:17px;letter-spacing:-0.03em}
.foot-links{position:absolute;left:428px;top:287px;list-style:none;font-family:"Poppins",sans-serif;font-size:13px;line-height:26.6px}
.contact-item{position:absolute;left:633px;display:flex;gap:10px;font-family:"Poppins",sans-serif;font-size:11px;line-height:15px}
.contact-item svg{flex:none;margin-top:2px}
.follow{position:absolute;top:3472px;width:32px;height:32px;border-radius:50%;background:var(--chip)}
.copyright{position:absolute;top:3741px;font-family:"Poppins",sans-serif;font-size:12px;color:var(--white)}
</style>
</head>
<body>

<header class="hero">
  <div class="brand"><div class="brand-dot"></div><span class="brand-name">Kavora PR</span></div>

  <nav class="nav">
    <svg width="16" height="16" viewBox="0 0 16 16" aria-label="Home"><path d="M8 1 L15 8 H13 V15 H10 V10 H6 V15 H3 V8 H1 Z" fill="#e5000f"/></svg>
    <a>Who We Are<span class="caret">⌄</span></a>
    <a>Our Expertise</a>
    <a>News</a>
    <a>Our work</a>
    <a>KavoraLink</a>
    <a>Contact</a>
    <a><span class="flag"></span>EN<span class="caret">⌄</span></a>
  </nav>
  <a class="btn" style="left:989px;top:32px;width:121px;height:46px">Contact Us</a>

  <h1 class="display hero-title" style="top:190px">We Are <span class="accent">Building</span><br>Relationships</h1>
  <p class="hero-copy">Thinking beyond media relations and marketing services, we understand the needs of our clients, and our experts and our creative staff are working on building long-term relationships. Anywhere in the world.</p>
  <a class="btn" style="left:526px;top:432px;width:148px;height:45px">Explore More</a>
</header>
<div class="photo hero-photo" role="img" aria-label="Photo of a team meeting around a table while a colleague presents charts on a monitor"></div>

<section aria-labelledby="who-title">
  <div class="who-mark"><span>Kavora PR</span></div>
  <p class="eyebrow abs" style="left:596px;top:1130px">Who We Are</p>
  <h2 id="who-title" class="display section-title abs" style="left:596px;top:1155px">We Are Creating<br>Unique Values.</h2>
  <p class="body-copy abs" style="left:596px;top:1259px;width:420px">Our experts, creative staff and data analysts are up to the most extraordinary challenges on all parts of the world. This is not only the beginning of a business relationship, for us, it means much more.</p>
  <a class="btn" style="left:596px;top:1339px;width:150px;height:44px">Explore More</a>
</section>

<section class="expertise" aria-labelledby="exp-title">
  <h2 id="exp-title" class="display section-title abs" style="left:89px;top:80px;color:var(--white)">Our Expertise</h2>
  <p class="abs" style="left:89px;top:142px;width:440px;font-size:13px;line-height:20.5px;color:var(--white)">To make choosing much easier for You, we provide the widest possible range of services. Let it be media relations, crisis management or marketing services, our experts are always available.</p>
  <a class="btn" style="left:949px;top:147px;width:161px;height:46px">Explore More
    <svg width="12" height="12" viewBox="0 0 12 12" aria-hidden="true"><path d="M2 10 L10 2 M4 2 H10 V8" stroke="#fff" stroke-width="1.4" fill="none"/></svg></a>

  <div class="tile" style="left:0;width:294px;background:linear-gradient(180deg,#6d6a66,#2a2826)" role="img" aria-label="Photo of a woman packing products in a boutique">
    <p class="tile-label">Consumer<br>Products &amp; Services</p></div>
  <div class="tile" style="left:294px;width:305px;background:linear-gradient(180deg,#4a4a4c,#1f1f21)" role="img" aria-label="Photo of a designer reviewing printed layouts">
    <p class="tile-label">Content &amp;<br>Publishing Strategy</p></div>
  <div class="tile" style="left:599px;width:305px;background:linear-gradient(180deg,#9a9894,#3a3836)" role="img" aria-label="Photo of a stressed businessman with colleagues behind him">
    <p class="tile-label">Crisis<br>Management</p></div>
  <div class="tile" style="left:904px;width:296px;background:linear-gradient(180deg,#5c5a60,#242326)" role="img" aria-label="Photo of a team discussing around a presentation screen">
    <p class="tile-label">Change<br>Management</p></div>
</section>

<section aria-labelledby="news-title">
  <h2 id="news-title" class="display section-title abs" style="left:0;width:1200px;text-align:center;top:2242px">News</h2>
  <p class="body-copy abs" style="left:230px;width:740px;top:2297px;text-align:center">It is a long established fact that a reader will be distracted by the readable content of a page when looking at its layout. The point of using Lorem Ipsum is that it has a more-or-less normal distribution of letters,...</p>
  <div class="news-card" style="left:89px;background:linear-gradient(160deg,#cfd3d6,#6f6b66)" role="img" aria-label="Photo of a woman presenting a chart on a flip board"></div>
  <div class="news-card" style="left:434px;background:linear-gradient(160deg,#dcdde0,#8b8e96)" role="img" aria-label="Photo of two colleagues reviewing printed charts at a desk"></div>
  <div class="news-card" style="left:779px;background:linear-gradient(160deg,#b9bcbd,#4e4136)" role="img" aria-label="Photo of two men working on a laptop at a wooden table"></div>
  <p class="news-caption" style="left:89px">Great Services!</p>
  <p class="news-caption" style="left:434px">Good Quality work!</p>
  <p class="news-caption" style="left:779px">Top Notch!</p>
</section>

<div class="abs" style="left:0;top:2764px;width:1200px;height:1px;background:var(--line)"></div>

<section aria-label="Social media">
  <div class="social-band" aria-hidden="true"><p class="social-word">Social Media</p></div>
  <p class="abs" style="left:0;width:1200px;text-align:center;top:2983px;font-family:'Poppins',sans-serif;font-weight:600;font-size:21px">KavoraLink</p>
  <a class="social-btn" style="left:452px;background:#3b5a96" aria-label="Social profile one"></a>
  <a class="social-btn" style="left:529px;background:#35a7e2" aria-label="Social profile two"></a>
  <a class="social-btn" style="left:605px;background:#26639e" aria-label="Social profile three"></a>
  <a class="social-btn" style="left:681px;background:#d32430" aria-label="Social profile four"></a>
</section>

<footer class="footer">
  <h2 class="display abs" style="left:88px;top:61px;font-size:44px;line-height:48px">Get in touch with us</h2>
  <a class="btn" style="left:989px;top:61px;width:121px;height:45px">Contact Us</a>
  <div class="abs" style="left:0;top:152px;width:1200px;height:1px;background:var(--footer-line)"></div>

  <div class="abs" style="left:165px;top:266px;width:188px;height:188px;border-radius:50%;background:var(--white);display:flex;align-items:center;justify-content:center">
    <span style="font-family:'Lexend Exa',sans-serif;font-weight:600;font-size:24px;color:var(--ink);letter-spacing:-0.04em">Kavora PR</span>
  </div>

  <h3 class="foot-head" style="left:428px">Useful Links</h3>
  <ul class="foot-links">
    <li>Home</li><li>Who We Are</li><li>Our Expertise</li><li>News</li><li>Our work</li><li>KavoraLink</li><li>Contact</li>
  </ul>

  <h3 class="foot-head" style="left:633px">contact info</h3>
  <div class="contact-item" style="top:305px">
    <svg width="13" height="10" viewBox="0 0 13 10" aria-hidden="true"><rect x=".5" y=".5" width="12" height="9" fill="#fff"/><path d="M.5 .5 L6.5 5.5 L12.5 .5" stroke="#1b1b1d" fill="none"/></svg>
    <span>Email:<br>info@example.com.au</span></div>
  <div class="contact-item" style="top:358px">
    <svg width="13" height="13" viewBox="0 0 13 13" aria-hidden="true"><path d="M2 1 L5 1 L6 4 L4 5.5 C5 7.5 6 8.5 8 9.5 L9.5 7.5 L12 8.5 L12 11.5 C6 12 1 7 2 1 Z" fill="#fff"/></svg>
    <span>Phone:<br>+08 123 456 7890</span></div>
  <div class="contact-item" style="top:412px">
    <svg width="11" height="15" viewBox="0 0 11 15" aria-hidden="true"><path d="M5.5 0 C2.5 0 0 2.4 0 5.4 C0 9.5 5.5 15 5.5 15 C5.5 15 11 9.5 11 5.4 C11 2.4 8.5 0 5.5 0 Z" fill="#fff"/><circle cx="5.5" cy="5.4" r="2" fill="#1b1b1d"/></svg>
    <span>Location:<br>Some address line goes here<br>city name country</span></div>

  <h3 class="foot-head" style="left:880px">Follow us</h3>
  <div class="abs" style="left:88px;top:544px;width:1022px;height:1px;background:var(--footer-line)"></div>
</footer>

<a class="follow" style="left:882px" aria-label="Social profile one"></a>
<a class="follow" style="left:922px" aria-label="Social profile two"></a>
<a class="follow" style="left:962px" aria-label="Social profile three"></a>
<a class="follow" style="left:1002px" aria-label="Social profile four"></a>

<p class="copyright" style="left:88px">© Copyright 2023 All Rights Reserved</p>
<p class="copyright" style="left:1018px">Privacy Policy</p>
<a class="abs" style="left:1138px;top:3706px;width:38px;height:38px;border-radius:50%;background:var(--chip);display:flex;align-items:center;justify-content:center" aria-label="Back to top">
  <svg width="10" height="6" viewBox="0 0 10 6" aria-hidden="true"><path d="M1 5 L5 1 L9 5" stroke="#fff" stroke-width="1.4" fill="none"/></svg>
</a>

</body>
</html>
```